lavieillelampe.com : "The old Lamp"

- Design: white background and a comfortable pillow with feathers coming out of the pillowcase

home for lavieillelampe (means "The old lamp)
( 1 image with a text recommending reading , the book of the week, the perfect match for your taste, your profile.. )
- Search engine on archives " Other small books " sorted by:
ß Alphabetically name authors
ß Last online
ß date ( and second access the date of the first edition)
ß Genre (poetry, novel, biography , autobiography , essay, young writers - with the possibility to add categories )
ß regions of the world (U.S. , UK , FR , Domaine Germanic , Domaine Hispanic , NL , CH, IT , UK , Asia, India , Africa, Caribbean - with the possibility to add categories ) .

- Section " box in quotes ", organized by themes ( - with ability to add themes) .

lavieillelampe.com ( Fr.)
Aimed to answer the question, " Wich book shall I read"

With a chart Embodying the choice is shades covers the first kind ( red for romance novels , for black font .. ) with shades and intensities based on different Criteria linked to personalized survey

Link blogs Lifestyle , Travel, Small World ..
Updates

Reason: Back from french Holidays we can now choose the best design. Have a glance at the already designed projects.!!!!

Target Market(s)

Niche of literacy. Customers who wish to know which book to read.
Customers who want to develop knowledge, and be considered as an elite, reading and knowing the right things

• Marché :
- Marché de niche : les Grands Amateurs
- Marché aspirationnel : signe de reconnaissance, connaisseurship (bagage culturel utile pour nouer une relation d’affaire , héritage de la Vieille Europe)

Industry/Entity Type

Travel

Font styles to use
Decorative
Script

```html
<!DOCTYPE html>
<html lang="en">
<head>
<meta charset="utf-8">
<title>The old Lamp — Home</title>
<link rel="stylesheet" href="https://fonts.googleapis.com/css2?family=Cinzel:wght@400;700&family=Didact+Gothic&family=Arimo:wght@400&display=swap">
<style>
  :root {
    --orange: #e8742a;
    --orange-deep: #c4571a;
    --rust: #8e3a0c;
    --peach: #fbe6d4;
    --ink: #4a4a4a;
    --text-grey: #7a7a7a;
    --field: #e9e9e9;
    --white: #ffffff;
    --heading-font: "Cinzel", serif;
    --body-font: "Didact Gothic", sans-serif;
    --ui-font: "Arimo", sans-serif;
  }
  * { box-sizing: border-box; margin: 0; padding: 0; }
  html, body { width: 1200px; height: 900px; overflow: hidden; background: var(--white); }
  body { position: relative; font-family: var(--body-font); color: var(--ink); }

  .top-rule { position: absolute; left: 0; top: 0; width: 1200px; height: 6px; background: #e2e2e2; }

  .site-header { position: absolute; left: 0; top: 6px; width: 1200px; height: 102px; }
  .brand { position: absolute; left: 100px; top: 32px; display: flex; align-items: center; gap: 10px;
    font-family: var(--heading-font); font-size: 32px; color: var(--orange-deep); letter-spacing: .5px; }
  .brand-dot { width: 13px; height: 13px; border-radius: 50%; background: var(--orange); }
  .account { position: absolute; left: 972px; top: 18px; display: flex; align-items: center; gap: 8px;
    font-family: var(--ui-font); font-size: 13px; }
  .account .login { background: #ececec; color: #333; padding: 2px 9px; border-radius: 2px; }
  .account .sep { color: #ccc; }
  .account .register { color: var(--orange); }
  .search { position: absolute; left: 826px; top: 54px; display: flex; }
  .search .field { width: 242px; height: 24px; background: var(--field); font-family: var(--ui-font);
    font-size: 12px; color: #aaa; padding: 5px 12px; }
  .search .go { width: 29px; height: 24px; margin-left: 2px; background: var(--orange); display: flex;
    align-items: center; justify-content: center; }

  .header-band { position: absolute; left: 0; top: 108px; width: 1200px; height: 8px;
    background: linear-gradient(90deg, #fde3cf, var(--peach) 60%, #fff3dc); }

  .hero { position: absolute; left: 0; top: 116px; width: 1200px; height: 312px;
    background: linear-gradient(90deg, #c9925c 0%, #e5782f 18%, #ef8a3a 45%, #e07a35 65%, #d99a6c 85%, #c88e6a 100%); }
  .hero-title { position: absolute; left: 183px; top: 130px; font-family: var(--heading-font);
    color: #fbeee3; font-size: 46px; line-height: 1; letter-spacing: 0; white-space: nowrap;
    text-shadow: 0 2px 3px rgba(120,50,10,.35); }
  .hero-title .initial { font-size: 66px; }
  .hero-sub { position: absolute; left: 428px; top: 195px; width: 154px; text-align: right;
    font-family: var(--ui-font); color: #fbeee3; font-size: 27px; letter-spacing: 1px; white-space: nowrap;
    text-shadow: 0 2px 3px rgba(120,50,10,.35); }
  .hero-frame { position: absolute; left: 592px; top: 35px; width: 208px; height: 234px;
    border-left: 1px solid #5a2a10; border-top: 1px solid #5a2a10; }
  .hero-frame::after { content: ""; position: absolute; right: -1px; top: 0; height: 8px; border-right: 1px solid #5a2a10; }
  .hero-books { position: absolute; left: 698px; top: 93px; width: 180px; height: 176px; background: var(--white);
    box-shadow: 3px 3px 4px rgba(0,0,0,.35); padding: 10px; }
  .hero-books div { width: 100%; height: 100%; background: linear-gradient(180deg, #d9d2c7, #8fc94a 55%, #3a8fd8 75%, #f07a2a); }
  .hero-reader { position: absolute; left: 558px; top: 222px; width: 140px; height: 120px; border-radius: 14px;
    background: linear-gradient(180deg, rgba(246,210,42,.85) 0%, rgba(235,120,40,.8) 50%, rgba(200,50,35,.9) 100%); }
  .hero-shadow { position: absolute; left: 110px; top: 428px; width: 980px; height: 10px;
    background: radial-gradient(ellipse at 50% 0, rgba(0,0,0,.35), transparent 70%); }

  .section-title { position: absolute; left: 100px; font-family: var(--heading-font); font-weight: 400;
    font-size: 20px; color: #4d4d4d; letter-spacing: .5px; white-space: nowrap; }
  .section-title em { font-style: normal; color: var(--orange); }
  .welcome-title { top: 465px; }
  .welcome-text { position: absolute; left: 100px; top: 501px; width: 1000px; font-size: 13.6px;
    line-height: 21px; color: var(--text-grey); text-align: justify; }
  .more-link { position: absolute; right: 102px; font-family: var(--heading-font); font-weight: 700;
    font-size: 12px; color: var(--orange-deep); letter-spacing: .5px; }
  .read-more { top: 571px; }
  .divider { position: absolute; left: 340px; top: 599px; width: 580px; height: 1px;
    background: linear-gradient(90deg, transparent, #e4e4e4, transparent); }
  .favorites-title { top: 625px; }

  .alphabet { position: absolute; left: 100px; top: 664px; width: 1000px; height: 142px; display: flex;
    background: var(--orange-deep); }
  .alphabet .letter { width: 27.75px; flex: none; background: var(--s); position: relative; font-family: var(--heading-font);
    font-weight: 700; font-size: 14px; color: var(--white); }
  .alphabet .letter span { position: absolute; bottom: 6px; left: 0; width: 100%; text-align: center; }
  .alphabet .letter.dark-text { color: #3a2a20; }
  .alphabet .letter.current { width: 25px; background: var(--orange); }
  .alphabet .letter.last { width: 24px; background: transparent; }
  .alphabet .letter.last span { background: #3a3a3a; width: 19px; left: 2px; bottom: 5px; }
  .shelf { position: absolute; left: 741px; top: 15px; width: 230px; height: 112px; background: #ececec;
    border-radius: 3px; display: flex; gap: 10px; padding: 10px 13px; }
  .shelf .cover { width: 60px; height: 92px; box-shadow: 2px 2px 3px rgba(0,0,0,.4); }
  .cover.blue { background: linear-gradient(160deg, #3d8fd0, #1b3f7a); }
  .cover.cream { background: linear-gradient(160deg, #efe7b8, #b9ad76); }
  .cover.red { background: linear-gradient(160deg, #c93a26, #6e1510); }
  .more-books { top: 824px; }

  .site-footer { position: absolute; left: 0; top: 862px; width: 1200px; height: 38px; background: var(--rust);
    font-family: var(--ui-font); font-size: 12px; color: var(--white); padding: 14px 100px; }
  .site-footer .domain { color: #ffd21a; }
</style>
</head>
<body>
  <div class="top-rule"></div>

  <header class="site-header">
    <div class="brand"><span>The old Lamp</span><span class="brand-dot"></span></div>
    <nav class="account"><span class="login">LogIn</span><span class="sep">|</span><span class="register">Register</span></nav>
    <div class="search">
      <div class="field">Type Your Words here......</div>
      <div class="go">
        <svg width="16" height="16" viewBox="0 0 16 16"><circle cx="7" cy="7" r="5" fill="none" stroke="#fff" stroke-width="2"/><line x1="10.5" y1="10.5" x2="14.5" y2="14.5" stroke="#fff" stroke-width="2.2" stroke-linecap="round"/></svg>
      </div>
    </div>
  </header>
  <div class="header-band"></div>

  <section class="hero" role="img" aria-label="Warm orange photo of an open book with fanned pages and a young woman reading">
    <div class="hero-frame"></div>
    <div class="hero-title"><span class="initial">C</span>OLLECTION</div>
    <div class="hero-sub">OF BOOKS</div>
    <div class="hero-books"><div role="img" aria-label="Illustration of a colourful stack of books with ladders"></div></div>
    <div class="hero-reader" role="img" aria-label="Cartoon mascot reading an open red book"></div>
  </section>
  <div class="hero-shadow"></div>

  <h2 class="section-title welcome-title">WELCOME TO <em>OUR SITE</em></h2>
  <p class="welcome-text">It is a long established fact that a reader will be distracted by the readable content of a page when looking at its layout. The point of using Lorem Ipsum is that it has a more-or-less normal distribution of letters, as opposed to using 'Content here, content here', making it look like readable English. Many desktop publishing packages and web page editors now use Lorem Ipsum .</p>
  <a class="more-link read-more">READ MORE</a>
  <div class="divider"></div>

  <h2 class="section-title favorites-title">YOUR <em>FAVORITE BOOKS</em></h2>
  <div class="alphabet">
    <div class="letter dark-text" style="--s:#f1f1f1"><span>A</span></div>
    <div class="letter dark-text" style="--s:#e6e6e6"><span>B</span></div>
    <div class="letter dark-text" style="--s:#dadada"><span>C</span></div>
    <div class="letter" style="--s:#cfcfcf"><span>D</span></div>
    <div class="letter" style="--s:#c3c3c3"><span>E</span></div>
    <div class="letter" style="--s:#b7b7b7"><span>F</span></div>
    <div class="letter" style="--s:#acacac"><span>G</span></div>
    <div class="letter" style="--s:#a0a0a0"><span>H</span></div>
    <div class="letter" style="--s:#949494"><span>I</span></div>
    <div class="letter" style="--s:#898989"><span>J</span></div>
    <div class="letter" style="--s:#7d7d7d"><span>K</span></div>
    <div class="letter" style="--s:#717171"><span>L</span></div>
    <div class="letter" style="--s:#666666"><span>M</span></div>
    <div class="letter" style="--s:#5a5a5a"><span>N</span></div>
    <div class="letter" style="--s:#4e4e4e"><span>O</span></div>
    <div class="letter" style="--s:#434343"><span>P</span></div>
    <div class="letter" style="--s:#373737"><span>Q</span></div>
    <div class="letter" style="--s:#2e2e2e"><span>R</span></div>
    <div class="letter" style="--s:#262626"><span>S</span></div>
    <div class="letter" style="--s:#1f1f1f"><span>T</span></div>
    <div class="letter" style="--s:#191919"><span>U</span></div>
    <div class="letter" style="--s:#121212"><span>V</span></div>
    <div class="letter" style="--s:#0a0a0a"><span>W</span></div>
    <div class="letter" style="--s:#000000"><span>X</span></div>
    <div class="letter current"><span>Y</span></div>
    <div class="letter last"><span>Z</span></div>
    <div class="shelf">
      <div class="cover blue" role="img" aria-label="Book cover, blue science-fiction artwork"></div>
      <div class="cover cream" role="img" aria-label="Book cover, cream illustrated artwork"></div>
      <div class="cover red" role="img" aria-label="Book cover, red creature artwork"></div>
    </div>
  </div>
  <a class="more-link more-books">MORE BOOKS</a>

  <footer class="site-footer">Copyright © 2014 <span class="domain">lavieillelampe.com</span> | All Rights Reserved | Privacy Policy</footer>
</body>
</html>
```